Up and coming Australian Systems Integrator needs a proposal template refresh

We need to update our proposal template and are looking for a fresh, modern, simple and elegant proposal template. We'd like to keep our existing logos if possible.
Quorvex is a privately owned company operating since 2006. Offices and technical staff located in Port Melbourne and Bendigo
Sustained, profitable growth year on year
Velmar strategic partner
Velmar Advanced Enterprise Network Architecture Specialisation
Velmar Advanced Security Architecture Specialisation
Velmar Advanced Collaboration Architecture Specialisation
Velmar Advanced Unified Computing Technology Specialisation
Velmar Advanced Data Centre Architecture Specialisation (in progress)
Velmar Gold Partner – Expect 2H2018
As well as being a Velmar partner we have a well established stable of other vendors such as Brandova, Teskaro, Haldenworth, ZEP, Mirvale Interactive, Dulm, TidePoint, KoMELDA Gate)
We are a top two provider of Velmar product/services in the Victorian healthcare sector.
Please feel free to use different colors and fonts as we feel the existing ones look dated.

```html
<!DOCTYPE html>
<html lang="en">
<head>
<meta charset="utf-8">
<title>Quorvex Proposal Template</title>
<link href="https://fonts.googleapis.com/css2?family=Montserrat:wght@700&family=Raleway:wght@300;400;700&family=Questrial&display=swap" rel="stylesheet">
<style>
  :root {
    --brand-blue: #1f4e9c;
    --ink: #2b2b2b;
    --muted: #7a7a7a;
    --panel-grey: #d2dae3;
    --row-grey: #e3e8ee;
    --paper: #ffffff;
    --stage: #2a2a2c;
  }
  * { box-sizing: border-box; margin: 0; padding: 0; }
  html, body { width: 1200px; height: 1200px; overflow: hidden; }
  body { background: var(--stage); position: relative; font-family: 'Questrial', sans-serif; color: var(--ink); }

  .page { position: absolute; background: var(--paper); overflow: hidden; }
  .page--contents { left: 40px; top: 40px; width: 540px; height: 780px; }
  .page--body { left: 615px; top: 340px; width: 550px; height: 820px; }

  .masthead { height: 96px; display: flex; align-items: flex-end; padding: 0 0 14px 40px; gap: 12px; }
  .masthead__mark { width: 22px; height: 22px; background: var(--brand-blue); }
  .masthead__name { font-family: 'Raleway', sans-serif; font-weight: 400; font-size: 44px; letter-spacing: 2px; color: var(--brand-blue); line-height: 1; }

  .confidential-band { background: var(--brand-blue); color: #fff; font-family: 'Montserrat', sans-serif; font-weight: 700; font-size: 13px; letter-spacing: .3px; text-align: center; height: 30px; line-height: 30px; }

  .page-title { font-family: 'Raleway', sans-serif; font-weight: 300; color: var(--brand-blue); text-align: center; }
  .page--contents .page-title { font-size: 28px; padding: 14px 0 10px; }
  .title-rule { height: 22px; background: var(--panel-grey); }

  .toc { list-style: none; font-family: 'Raleway', sans-serif; color: var(--muted); font-size: 15px; }
  .toc__item { display: flex; align-items: baseline; padding: 8px 40px 8px 30px; }
  .toc__item--level1 { background: var(--row-grey); color: var(--brand-blue); font-weight: 700; font-size: 16px; padding-top: 10px; }
  .toc__item--level2 { padding-left: 38px; }
  .toc__item--level3 { padding-left: 56px; }
  .toc__leader { flex: 1; border-bottom: 1px dotted #999; margin: 0 4px; transform: translateY(-4px); }
  .toc__page { font-weight: 400; color: var(--muted); }

  .backdrop-pattern { position: absolute; left: 0; right: 0; bottom: 0; height: 300px;
    background: linear-gradient(180deg, rgba(240,243,247,0) 0%, #f1f3f6 100%); }

  .footer-mark { position: absolute; font-family: 'Questrial', sans-serif; color: var(--muted); font-size: 14px; letter-spacing: .3px; }
  .page--contents .footer-mark { right: 60px; bottom: 50px; }
  .page--body .footer-mark { left: 300px; bottom: 50px; }
  .page-number { position: absolute; right: 40px; bottom: 22px; font-size: 9px; color: var(--muted); }

  .sidebar { position: absolute; left: 0; top: 176px; bottom: 0; width: 200px; background: var(--panel-grey); padding: 16px 16px; font-size: 9px; line-height: 1.3; color: #333; text-align: center; }
  .page--body .page-title { position: absolute; left: 200px; right: 0; top: 138px; font-size: 28px; }
  .main-copy { position: absolute; left: 222px; right: 28px; top: 186px; font-size: 11.5px; line-height: 1.32; text-align: justify; color: #222; }
  .main-copy p { margin-bottom: 16px; text-indent: 20px; }
</style>
</head>
<body>

<section class="page page--contents">
  <header class="masthead">
    <span class="masthead__mark"></span>
    <span class="masthead__name">QUORVEX</span>
  </header>
  <div class="confidential-band">COMMERCIAL-IN CONFIDENCE</div>
  <h1 class="page-title">TABLE OF CONTENTS</h1>
  <div class="title-rule"></div>
  <ol class="toc">
    <li class="toc__item toc__item--level1"><span>1 HEADING</span><span class="toc__leader"></span><span class="toc__page">2</span></li>
    <li class="toc__item toc__item--level2"><span>1.1 Heading</span><span class="toc__leader"></span><span class="toc__page">5</span></li>
    <li class="toc__item toc__item--level3"><span>1.1.1 Heading</span><span class="toc__leader"></span><span class="toc__page">8</span></li>
    <li class="toc__item toc__item--level3"><span>1.1.2 Heading</span><span class="toc__leader"></span><span class="toc__page">10</span></li>
    <li class="toc__item toc__item--level3"><span>1.1.3 Heading</span><span class="toc__leader"></span><span class="toc__page"></span></li>
  </ol>
  <div class="backdrop-pattern" role="img" aria-label="Faint geometric network line pattern"></div>
  <div class="footer-mark">COMMERCIAL-IN-CONFIDENCE</div>
</section>

<section class="page page--body">
  <header class="masthead">
    <span class="masthead__mark"></span>
    <span class="masthead__name">QUORVEX</span>
  </header>
  <div class="confidential-band">COMMERCIAL-IN CONFIDENCE</div>
  <aside class="sidebar">Lorem ipsum dolor sit amet, consectetur adipiscing elit. Pellentesque commodo ullamcorper molestie. Cras vitae ante eu nisi efficitur rutrum. Sed egestas quis lectus quis faucibus. Quisque vitae tincidunt massa. Maecenas ullamcorper blandit nisl. Ut ac sem ac lectus fringilla iaculis. Aliquam condimentum ut magna et consequat.</aside>
  <h2 class="page-title">HEADING</h2>
  <div class="main-copy">
    <p>Lorem ipsum dolor sit amet, consectetur adipiscing elit. Pellentesque commodo ullamcorper molestie. Cras vitae ante eu nisi efficitur rutrum. Sed egestas quis lectus quis faucibus. Quisque vitae tincidunt massa. Quisque sagittis ipsum quis ligula auctor, eu aliquam enim rutrum. Aenean tortor turpis, placerat ut pulvinar ac, finibus ut augue. In a dignissim nisi. Duis a faucibus mauris. Fusce sed purus vitae orci pharetra bibendum.</p>
    <p>Donec luctus sit amet mi et commodo. Suspendisse et volutpat justo. Duis volutpat eros et nulla finibus blandit. Donec auctor fermentum erat sit amet pellentesque. Aliquam at semper massa, a porttitor neque. Proin lobortis, erat dignissim euismod commodo, enim quam pretium enim, vitae tincidunt enim ligula non sapien. Phasellus finibus, sem vitae ultricies fringilla, risus tortor rhoncus quam, sit amet mollis nisl neque quis velit. Aliquam finibus urna vehicula ex aliquet, quis viverra urna ornare. Duis porta arcu ultricies massa suscipit posuere.</p>
    <p>Quisque nec ex massa. Donec tincidunt accumsan mattis. Phasellus laoreet eleifend bibendum. Integer tortor nisl, cursus ut arcu eget, faucibus congue mi. Mauris risus nibh, elementum eu turpis vitae, congue iaculis odio. Quisque viverra justo at venenatis dictum. Aliquam finibus sagittis mi eu viverra. Maecenas ullamcorper blandit nisl. Ut ac sem ac lectus fringilla iaculis. Aliquam condimentum ut magna et consequat.</p>
  </div>
  <div class="backdrop-pattern" role="img" aria-label="Faint geometric network line pattern"></div>
  <div class="footer-mark">COMMERCIAL-IN-CONFIDENCE</div>
  <div class="page-number">Page 2 of 4</div>
</section>

</body>
</html>
```